UI Mockup For Online Scheduling Software

11.01.2018 - Brief Update:
The brief has not changed but the summary below as being added to aid designers.

- New file added "Updated 11.01.2018 - Individual Box" to clarify the sections. Specifically the primary tag section
- Improve on the current styling
- Consider changing the section layout to maximise the number of blocks displayed on screen (The sections dont not need to be stacked like the current version.
- The design is for the application running on a desktop PC with 16:9 screen aspect
- The design styling/layout should not look like the current version
- You may use the application to get an understanding of its workings at this link....https://tomsbrevik.lqnhosting.com.au/
- Think outside the box....use your creative flare and show me something different to the current app (style and layout)

There are already some good submissions so closer to the deadline I will increase the budget and award $$$ to 1st and 2nd. The winner will be chosen to directly work on the remaining aspects of this application (setting page, mobile design, dashboard etc). The next design project associated to this application will be 10 time bigger than this one.

Good Luck Designers

*************************************************************
Redesign the user interface to make more efficient use of the screen real estate.

The software works by adding (Drag & Drop) Project Blocks to a Date Section. Then tags are added (Drag & Drop) to the block section below the header, and then resources are added to the block section below the tags.
Each block has 4 main sections that are stacked vertically:

1. Header - Displays Title and Address
2. Tags - Displays tags, maximum of 6 tags
3. Resources - Displays resources, maximum of 10 resources, NOTE: this section can be hidded.
4. Footer - Display basic stats (eg. 3 Resources assigned)

It is critical that as many block (20-30) as possible for a single date can be visible on screen.

The following criteria must be considered when mocking up layout:
1. Font Type, size, colour and emphasis
2. Block Colour/Shading, borders ect
3. Section Layout within the block (stacking & Alignment)
4. Mock ups to show scaled layout of blocks in both the open state and Closed State.
5. Mock up to display a minimum of 20 blocks.
6. Create a variation of your design that adds a 5th section. This will display the first tag only:
1. Header - Always Visible
2. Primary Tag - Always Visible
3. Secondary Tags - Can be hidden
4. Resources - Can be Hidden
5. Footer - Can be Hidden

Please be creative with your design and layout. I like a clean, minimalist design.
At this stage CSS file will not be required but would be benificial

Target Market(s)

N/A

Industry/Entity Type

Software

Number of Pages Required

1 page

Font styles to use
Other font styles liked:
• Designers Choice

Colors

Designer to choose colors to be used in the design.

Requirements
Must have
• Variation to current layout and style
Should not have
• Same styling and layout as current design

```html
<!DOCTYPE html>
<html lang="en">
<head>
<meta charset="utf-8">
<title>Daily Schedule Board</title>
<link href="https://fonts.googleapis.com/css2?family=Questrial&display=swap" rel="stylesheet">
<style>
:root{
  --page:#ffffff;
  --frame:#e2e2e2;
  --bar:#f2f2f2;
  --card-head:#f1f1f1;
  --card-line:#e4e4e4;
  --ink:#222222;
  --ink-soft:#555555;
  --ink-faint:#777777;
  --tag-trade:#2c3a4d;
  --tag-task:#2f88f6;
  --tag-start:#a531ec;
  --tag-ok:#24c23e;
  --tag-supplier:#f8ae27;
  --tag-note:#f52a2a;
}
*{box-sizing:border-box;margin:0;padding:0}
html,body{width:1200px;height:1000px;overflow:hidden;background:var(--page)}
body{font-family:"Questrial",sans-serif;color:var(--ink);position:relative}
.board{position:absolute;left:17px;top:20px;width:1166px;height:1000px;border:1px solid var(--frame);border-bottom:none;box-shadow:0 0 4px rgba(0,0,0,.12);overflow:hidden}
.topbar{height:62px;background:var(--bar);display:flex;align-items:center;padding-left:32px;box-shadow:0 2px 3px rgba(0,0,0,.12);position:relative;z-index:2}
.topbar .date{font-weight:700;font-size:17px;letter-spacing:1px;margin-left:24px;word-spacing:2px}
.topbar .stat{position:absolute;top:22px;font-size:14px;letter-spacing:.6px}
.comments{left:586px;display:flex;align-items:center;gap:6px}
.assigned{left:711px}
.scheduled{left:931px}
.grid{position:absolute;left:11px;top:86px;display:grid;grid-template-columns:repeat(6,179px);grid-auto-rows:252px;column-gap:14px;row-gap:13.5px}
.block{border:1px solid var(--card-line);box-shadow:0 1px 3px rgba(0,0,0,.14);display:flex;flex-direction:column;background:#fff}
.block-head{height:50px;background:var(--card-head);border-bottom:1px solid var(--card-line);padding:9px 9px 0;position:relative}
.block-title{font-weight:700;font-size:11.5px;letter-spacing:.4px;line-height:14px;color:#333;white-space:nowrap}
.block-address{font-size:9px;color:var(--ink-soft);line-height:12px;letter-spacing:.3px}
.block-gear{position:absolute;right:6px;top:27px;width:10px;height:10px;fill:#666}
.tags{padding:15px 9px 0;display:flex;flex-direction:column;gap:7px}
.tag{height:20px;border-radius:10px;color:#fff;font-size:11.5px;letter-spacing:.4px;display:flex;align-items:center;padding:0 8px 0 9px;position:relative;white-space:nowrap}
.tag::before{content:"";flex:none;width:11px;height:7px;background:#fff;margin-right:10px;clip-path:polygon(0 0,70% 0,100% 50%,70% 100%,0 100%)}
.tag .x{margin-left:auto;font-size:12px;line-height:1}
.trade{background:var(--tag-trade)}
.task{background:var(--tag-task)}
.start{background:var(--tag-start)}
.ok{background:var(--tag-ok)}
.supplier{background:var(--tag-supplier)}
.note{background:var(--tag-note)}
.resources{display:flex;justify-content:space-between;align-items:center;padding:0 12px 0 15px;margin-top:12px;font-size:11px;letter-spacing:1px;color:#333}
.resources::after{content:"";border-left:5px solid #444;border-top:4px solid transparent;border-bottom:4px solid transparent}
.block-foot{margin-top:auto;height:22px;border-top:1px solid var(--card-line);display:flex;justify-content:space-between;align-items:center;padding:0 8px 0 9px;font-size:9px;color:var(--ink-faint);letter-spacing:.3px}
</style>
</head>
<body>
<svg width="0" height="0" style="position:absolute">
  <symbol id="gear" viewBox="0 0 10 10"><path d="M4.2 0h1.6l.3 1.4 1 .5 1.2-.8 1.1 1.1-.8 1.2.5 1 1.4.3v1.6l-1.4.3-.5 1 .8 1.2-1.1 1.1-1.2-.8-1 .5-.3 1.4H4.2l-.3-1.4-1-.5-1.2.8-1.1-1.1.8-1.2-.5-1L0 5.8V4.2l1.4-.3.5-1-.8-1.2 1.1-1.1 1.2.8 1-.5zM5 3.4a1.6 1.6 0 1 0 0 3.2 1.6 1.6 0 0 0 0-3.2z"/></symbol>
</svg>
<div class="board">
  <header class="topbar">
    <svg width="20" height="22" viewBox="0 0 20 22" aria-hidden="true"><rect x="1" y="3" width="18" height="18" rx="2" fill="none" stroke="#333" stroke-width="2"/><rect x="1" y="3" width="18" height="5" fill="#333"/><rect x="5" y="0" width="2" height="5" fill="#333"/><rect x="13" y="0" width="2" height="5" fill="#333"/><rect x="5" y="11" width="4" height="3" fill="#333"/></svg>
    <span class="date">9th January, 2018 (Tuesday)</span>
    <span class="stat comments">Comments <svg width="10" height="6" viewBox="0 0 10 6"><path d="M0 0h10L5 6z" fill="#222"/></svg></span>
    <span class="stat assigned">Project assigned 15 of 67</span>
    <span class="stat scheduled">Resourses scheduled 50 of 55</span>
  </header>

  <main class="grid">
    <!-- row 1 -->
    <section class="block"><div class="block-head"><div class="block-title">21356 KLR NBD West-214k</div><div class="block-address">St. Glenbush</div><svg class="block-gear"><use href="#gear"/></svg></div><div class="tags"><div class="tag trade">Trade:Shortcrete<span class="x">×</span></div><div class="tag task">Task:Pilled walls<span class="x">×</span></div><div class="tag start">Start:6:45AM<span class="x">×</span></div><div class="tag ok">Confirmed<span class="x">×</span></div></div><div class="resources">Resources</div><div class="block-foot"><span>3 Resourses</span><span>0 Plant assigned</span></div></section>
    <section class="block"><div class="block-head"><div class="block-title">21425 Alderlea</div><div class="block-address">Brennall-42 marlow<br>st. Alderlea</div><svg class="block-gear"><use href="#gear"/></svg></div><div class="tags"><div class="tag trade">Trade:Shortcrete<span class="x">×</span></div><div class="tag supplier">Supplier:Stonecrest<span class="x">×</span></div><div class="tag start">Start:6:45AM<span class="x">×</span></div><div class="tag ok">Confirmed<span class="x">×</span></div></div><div class="resources">Resources</div><div class="block-foot"><span>3 Resourses</span><span>0 Plant assigned</span></div></section>
    <section class="block"><div class="block-head"><div class="block-title">21387 Merrivale</div><div class="block-address">Brennall-42 marlow<br>st. Alderlea</div><svg class="block-gear"><use href="#gear"/></svg></div><div class="tags"><div class="tag trade">Trade:Anchoring<span class="x">×</span></div><div class="tag task">Task::Drill&amp;Install<span class="x">×</span></div><div class="tag start">Start:6:45AM<span class="x">×</span></div><div class="tag ok">Confirmed<span class="x">×</span></div></div><div class="resources">Resources</div><div class="block-foot"><span>3 Resourses</span><span>0 Plant assigned</span></div></section>
    <section class="block"><div class="block-head"><div class="block-title">21478 Harbour park</div><div class="block-address">Brennall-42 marlow<br>st. Alderlea</div><svg class="block-gear"><use href="#gear"/></svg></div><div class="tags"><div class="tag trade">Trade:Anchoring<span class="x">×</span></div><div class="tag task">Task:Stressing<span class="x">×</span></div><div class="tag start">Start:6:45AM<span class="x">×</span></div><div class="tag ok">Confirmed<span class="x">×</span></div></div><div class="resources">Resources</div><div class="block-foot"><span>3 Resourses</span><span>0 Plant assigned</span></div></section>
    <section class="block"><div class="block-head"><div class="block-title">21478 Harbour park</div><div class="block-address">Brennall-42 marlow<br>st. Alderlea</div><svg class="block-gear"><use href="#gear"/></svg></div><div class="tags"><div class="tag trade">Trade:Steel<span class="x">×</span></div><div class="tag task">Task:Stressing<span class="x">×</span></div><div class="tag note">Note:NightShift<span class="x">×</span></div><div class="tag start">Start:6:45AM<span class="x">×</span></div><div class="tag ok">Confirmed<span class="x">×</span></div></div><div class="resources">Resources</div><div class="block-foot"><span>3 Resourses</span><span>0 Plant assigned</span></div></section>
    <section class="block"><div class="block-head"><div class="block-title">21478 Harbour park</div><div class="block-address">Brennall-42 marlow<br>st. Alderlea</div><svg class="block-gear"><use href="#gear"/></svg></div><div class="tags"><div class="tag trade">Trade:Steel<span class="x">×</span></div><div class="tag task">Task:Stressing<span class="x">×</span></div><div class="tag start">Start:6:45AM<span class="x">×</span></div><div class="tag ok">Confirmed<span class="x">×</span></div></div><div class="resources">Resources</div><div class="block-foot"><span>3 Resourses</span><span>0 Plant assigned</span></div></section>

    <!-- row 2 -->
    <section class="block"><div class="block-head"><div class="block-title">21356 KLR NBD West-214k</div><div class="block-address">St. Glenbush</div><svg class="block-gear"><use href="#gear"/></svg></div><div class="tags"><div class="tag trade">Trade:Shortcrete<span class="x">×</span></div><div class="tag task">Task:Pilled walls<span class="x">×</span></div><div class="tag start">Start:6:45AM<span class="x">×</span></div><div class="tag ok">Confirmed<span class="x">×</span></div></div><div class="resources">Resources</div><div class="block-foot"><span>3 Resourses</span><span>0 Plant assigned</span></div></section>
    <section class="block"><div class="block-head"><div class="block-title">21425 Alderlea</div><div class="block-address">Brennall-42 marlow<br>st. Alderlea</div><svg class="block-gear"><use href="#gear"/></svg></div><div class="tags"><div class="tag trade">Trade:Shortcrete<span class="x">×</span></div><div class="tag supplier">Supplier:Stonecrest<span class="x">×</span></div><div class="tag start">Start:6:45AM<span class="x">×</span></div><div class="tag ok">Confirmed<span class="x">×</span></div></div><div class="resources">Resources</div><div class="block-foot"><span>3 Resourses</span><span>0 Plant assigned</span></div></section>
    <section class="block"><div class="block-head"><div class="block-title">21387 Merrivale</div><div class="block-address">Brennall-42 marlow<br>st. Alderlea</div><svg class="block-gear"><use href="#gear"/></svg></div><div class="tags"><div class="tag trade">Trade:Anchoring<span class="x">×</span></div><div class="tag task">Task::Drill&amp;Install<span class="x">×</span></div><div class="tag start">Start:6:45AM<span class="x">×</span></div><div class="tag ok">Confirmed<span class="x">×</span></div></div><div class="resources">Resources</div><div class="block-foot"><span>3 Resourses</span><span>0 Plant assigned</span></div></section>
    <section class="block"><div class="block-head"><div class="block-title">21478 Harbour park</div><div class="block-address">Brennall-42 marlow<br>st. Alderlea</div><svg class="block-gear"><use href="#gear"/></svg></div><div class="tags"><div class="tag trade">Trade:Anchoring<span class="x">×</span></div><div class="tag task">Task:Stressing<span class="x">×</span></div><div class="tag start">Start:6:45AM<span class="x">×</span></div><div class="tag ok">Confirmed<span class="x">×</span></div></div><div class="resources">Resources</div><div class="block-foot"><span>3 Resourses</span><span>0 Plant assigned</span></div></section>
    <section class="block"><div class="block-head"><div class="block-title">21478 Harbour park</div><div class="block-address">Brennall-42 marlow<br>st. Alderlea</div><svg class="block-gear"><use href="#gear"/></svg></div><div class="tags"><div class="tag trade">Trade:Steel<span class="x">×</span></div><div class="tag task">Task:Stressing<span class="x">×</span></div><div class="tag note">Note:NightShift<span class="x">×</span></div><div class="tag start">Start:6:45AM<span class="x">×</span></div><div class="tag ok">Confirmed<span class="x">×</span></div></div><div class="resources">Resources</div><div class="block-foot"><span>3 Resourses</span><span>0 Plant assigned</span></div></section>
    <section class="block"><div class="block-head"><div class="block-title">21478 Harbour park</div><div class="block-address">Brennall-42 marlow<br>st. Alderlea</div><svg class="block-gear"><use href="#gear"/></svg></div><div class="tags"><div class="tag trade">Trade:Steel<span class="x">×</span></div><div class="tag task">Task:Stressing<span class="x">×</span></div><div class="tag start">Start:6:45AM<span class="x">×</span></div><div class="tag ok">Confirmed<span class="x">×</span></div></div><div class="resources">Resources</div><div class="block-foot"><span>3 Resourses</span><span>0 Plant assigned</span></div></section>

    <!-- row 3 -->
    <section class="block"><div class="block-head"><div class="block-title">21356 KLR NBD West-214k</div><div class="block-address">St. Glenbush</div><svg class="block-gear"><use href="#gear"/></svg></div><div class="tags"><div class="tag trade">Trade:Shortcrete<span class="x">×</span></div><div class="tag task">Task:Pilled walls<span class="x">×</span></div><div class="tag start">Start:6:45AM<span class="x">×</span></div><div class="tag ok">Confirmed<span class="x">×</span></div></div><div class="resources">Resources</div><div class="block-foot"><span>3 Resourses</span><span>0 Plant assigned</span></div></section>
    <section class="block"><div class="block-head"><div class="block-title">21425 Alderlea</div><div class="block-address">Brennall-42 marlow<br>st. Alderlea</div><svg class="block-gear"><use href="#gear"/></svg></div><div class="tags"><div class="tag trade">Trade:Shortcrete<span class="x">×</span></div><div class="tag supplier">Supplier:Stonecrest<span class="x">×</span></div><div class="tag start">Start:6:45AM<span class="x">×</span></div><div class="tag ok">Confirmed<span class="x">×</span></div></div><div class="resources">Resources</div><div class="block-foot"><span>3 Resourses</span><span>0 Plant assigned</span></div></section>
    <section class="block"><div class="block-head"><div class="block-title">21387 Merrivale</div><div class="block-address">Brennall-42 marlow<br>st. Alderlea</div><svg class="block-gear"><use href="#gear"/></svg></div><div class="tags"><div class="tag trade">Trade:Anchoring<span class="x">×</span></div><div class="tag task">Task::Drill&amp;Install<span class="x">×</span></div><div class="tag start">Start:6:45AM<span class="x">×</span></div><div class="tag ok">Confirmed<span class="x">×</span></div></div><div class="resources">Resources</div><div class="block-foot"><span>3 Resourses</span><span>0 Plant assigned</span></div></section>
    <section class="block"><div class="block-head"><div class="block-title">21478 Harbour park</div><div class="block-address">Brennall-42 marlow<br>st. Alderlea</div><svg class="block-gear"><use href="#gear"/></svg></div><div class="tags"><div class="tag trade">Trade:Anchoring<span class="x">×</span></div><div class="tag task">Task:Stressing<span class="x">×</span></div><div class="tag start">Start:6:45AM<span class="x">×</span></div><div class="tag ok">Confirmed<span class="x">×</span></div></div><div class="resources">Resources</div><div class="block-foot"><span>3 Resourses</span><span>0 Plant assigned</span></div></section>
    <section class="block"><div class="block-head"><div class="block-title">21478 Harbour park</div><div class="block-address">Brennall-42 marlow<br>st. Alderlea</div><svg class="block-gear"><use href="#gear"/></svg></div><div class="tags"><div class="tag trade">Trade:Steel<span class="x">×</span></div><div class="tag task">Task:Stressing<span class="x">×</span></div><div class="tag note">Note:NightShift<span class="x">×</span></div><div class="tag start">Start:6:45AM<span class="x">×</span></div><div class="tag ok">Confirmed<span class="x">×</span></div></div><div class="resources">Resources</div><div class="block-foot"><span>3 Resourses</span><span>0 Plant assigned</span></div></section>
    <section class="block"><div class="block-head"><div class="block-title">21478 Harbour park</div><div class="block-address">Brennall-42 marlow<br>st. Alderlea</div><svg class="block-gear"><use href="#gear"/></svg></div><div class="tags"><div class="tag trade">Trade:Steel<span class="x">×</span></div></div><div class="resources">Resources</div><div class="block-foot"><span>3 Resourses</span><span>0 Plant assigned</span></div></section>

    <!-- row 4 -->
    <section class="block"><div class="block-head"><div class="block-title">21356 KLR NBD West-214k</div><div class="block-address">St. Glenbush</div><svg class="block-gear"><use href="#gear"/></svg></div><div class="tags"><div class="tag trade">Trade:Shortcrete<span class="x">×</span></div><div class="tag task">Task:Pilled walls<span class="x">×</span></div></div></section>
    <section class="block"><div class="block-head"><div class="block-title">21425 Alderlea</div><div class="block-address">Brennall-42 marlow<br>st. Alderlea</div><svg class="block-gear"><use href="#gear"/></svg></div><div class="tags"><div class="tag trade">Trade:Shortcrete<span class="x">×</span></div><div class="tag supplier">Supplier:Stonecrest<span class="x">×</span></div></div></section>
    <section class="block"><div class="block-head"><div class="block-title">21387 Merrivale</div><div class="block-address">Brennall-42 marlow<br>st. Alderlea</div><svg class="block-gear"><use href="#gear"/></svg></div><div class="tags"><div class="tag trade">Trade:Anchoring<span class="x">×</span></div><div class="tag task">Task::Drill&amp;Install<span class="x">×</span></div></div></section>
    <section class="block"><div class="block-head"><div class="block-title">21478 Harbour park</div><div class="block-address">Brennall-42 marlow<br>st. Alderlea</div><svg class="block-gear"><use href="#gear"/></svg></div><div class="tags"><div class="tag trade">Trade:Anchoring<span class="x">×</span></div><div class="tag task">Task:Stressing<span class="x">×</span></div></div></section>
    <section class="block"><div class="block-head"><div class="block-title">21478 Harbour park</div><div class="block-address">Brennall-42 marlow<br>st. Alderlea</div><svg class="block-gear"><use href="#gear"/></svg></div><div class="tags"><div class="tag trade">Trade:Steel<span class="x">×</span></div><div class="tag task">Task:Stressing<span class="x">×</span></div></div></section>
    <section class="block"><div class="block-head"><div class="block-title">21478 Harbour park</div><div class="block-address">Brennall-42 marlow<br>st. Alderlea</div><svg class="block-gear"><use href="#gear"/></svg></div><div class="tags"><div class="tag trade">Trade:Steel<span class="x">×</span></div><div class="tag task">Task:Stressing<span class="x">×</span></div></div></section>
  </main>
</div>
</body>
</html>
```